Plumber needs a business card

I need a new business card for my plumbing business. I dont have a logo at the moment but I want business cards that are simple but very professional. I want to look like
Name: Mitch Dorley
Address: (just make one up)
Phone: 0455 318 726
Email: mitch@dorleymail.com
Colors to use:
Blacks, blues, silvers

```html
<!DOCTYPE html>
<html lang="en">
<head>
<meta charset="utf-8">
<title>Mitch Dorley – Business Card</title>
<link rel="stylesheet" href="https://fonts.googleapis.com/css2?family=Lato:wght@400;700&display=swap">
<style>
  :root {
    --page-bg: #e9e9eb;
    --card-black: #1c1c1d;
    --card-shadow: rgba(0, 0, 0, 0.28);
    --text-silver: #d4d4d6;
    --band-silver: #cfcfd1;
    --base-dark: #141415;
    --edge-blue: #2c4f9e;
    --edge-green: #3f9a3a;
  }
  html, body {
    margin: 0;
    padding: 0;
    width: 1200px;
    height: 900px;
    overflow: hidden;
    background: var(--page-bg);
  }
  .stage {
    width: 1200px;
    height: 900px;
    display: flex;
    align-items: center;
    justify-content: center;
  }
  .business-card {
    position: relative;
    width: 840px;
    height: 480px;
    background: var(--card-black);
    box-shadow: 0 18px 40px var(--card-shadow);
    font-family: "Lato", sans-serif;
    color: var(--text-silver);
    overflow: hidden;
  }
  .owner-name {
    position: absolute;
    left: 58px;
    bottom: 92px;
    margin: 0;
    font-size: 38px;
    font-weight: 700;
    letter-spacing: 0.5px;
  }
  .contact-block {
    position: absolute;
    right: 62px;
    top: 150px;
    text-align: right;
    font-size: 18px;
    line-height: 1.25;
  }
  .address {
    margin: 0 0 26px;
    font-style: normal;
  }
  .contact-line {
    display: flex;
    align-items: center;
    justify-content: flex-end;
    gap: 10px;
    margin: 0 0 4px;
  }
  .contact-icon {
    width: 18px;
    height: 18px;
    flex: none;
  }
  .footer-band {
    position: absolute;
    left: 0;
    right: 0;
    bottom: 0;
    height: 44px;
  }
  .footer-band .silver-stripe {
    height: 12px;
    background: var(--band-silver);
  }
  .footer-band .dark-base {
    height: 29px;
    background: var(--base-dark);
  }
  .footer-band .accent-edge {
    height: 3px;
    background: linear-gradient(90deg, var(--edge-green) 0%, var(--edge-green) 68%, var(--edge-blue) 68%, var(--edge-blue) 100%);
  }
</style>
</head>
<body>
  <main class="stage">
    <section class="business-card" aria-label="Business card of Mitch Dorley">
      <div class="contact-block">
        <address class="address">kessler mill road<br>westbrook,hollis</address>
        <p class="contact-line">
          <svg class="contact-icon" viewBox="0 0 18 18" aria-hidden="true">
            <rect x="5" y="1.5" width="8" height="15" rx="1.5" fill="none" stroke="currentColor" stroke-width="1.4"/>
            <line x1="5.5" y1="13" x2="12.5" y2="13" stroke="currentColor" stroke-width="1.2"/>
          </svg>
          <span>0455 318 726</span>
        </p>
        <p class="contact-line">
          <svg class="contact-icon" viewBox="0 0 18 18" aria-hidden="true">
            <rect x="1.5" y="4" width="15" height="10.5" fill="currentColor"/>
            <polyline points="1.5,4 9,10 16.5,4" fill="none" stroke="#1c1c1d" stroke-width="1.3"/>
          </svg>
          <span>mitch@dorleymail.com</span>
        </p>
      </div>
      <h1 class="owner-name">Mitch Dorley</h1>
      <div class="footer-band" aria-hidden="true">
        <div class="silver-stripe"></div>
        <div class="dark-base"></div>
        <div class="accent-edge"></div>
      </div>
    </section>
  </main>
</body>
</html>
```